Web design for online activity booking website

Our activity booking website uTrundle.net is looking outdated and needing a loving revamp on its design and STRUCTURE. it was initially created as a destination guide before we modified the homepage slightly to sell activities. So please DON'T RELY on the current website for your design. Now, the focus is ACTIVITY, while guide/ info should come only as secondary.

In other words, we will be doing something very similar to Plomaro.com (a bit crowded for our liking) and FindMyTrailpal.com. If you could capture the best essences of both, that would be awesome! Besides, we also like nestlo.com's simplicity.

SIMPLE, CLEAN, BRIGHT, USER and MOBILE FRIENDLY please :)

We have a new logo created and some wireframes (a few more in progress) so you know the basic components required in each page. These are just rough ideas so please ignore the ratio/size, colours etc and if you have a better way of arranging or simplifying things, please do so :)

Help us make it a website that everyone would love!

Thank you in advance for your time and artistry.

Target Market(s)

Internet savvy travellers between 18-65

Industry/Entity Type

Tourism

Number of Pages Required

5+ page

Requirements
Must have
• SIMPLE, CLEAN feel, USER and MOBILE FRIENDLY please :)
• See attachments for rough structure. Will also need standard pages such as:
• - About Us
• - Contact Us
• - Wishlist etc
• Message from our developer "designer to keep layers in PSD format accurately so html/css code does not need to lead a mess in photoshop"
Nice to have
• UPDATE: We are so thrilled to receive so many web designs but on the other hand, the submissions are getting too generic and everyone's designs is almost looking identical (many look like they are “borrowed” from existing popular websites). This is making the selection and decision process very difficult.
• So instead of sending us more of the very similar homepage design with minor tweaks (which we can do during handover section anyway), please send us a design of more specific page of our website. Please refer job brief, file no. 5 - Product detail page.
• This will give us better idea of your skills and choose the best as winner to work on the rest of our web pages.
Should not have
• No dark background please

```html
<!DOCTYPE html>
<html lang="en">
<head>
<meta charset="utf-8">
<title>uTrundle – Book Activities</title>
<link href="https://fonts.googleapis.com/css2?family=Open+Sans:wght@400;600;700&family=Roboto:wght@400;500;700&display=swap" rel="stylesheet">
<style>
:root{
  --purple:#5b2d7e;
  --purple-btn:#6a3a8e;
  --accent:#e8733a;
  --star:#f39c12;
  --light-bg:#ececec;
  --white:#ffffff;
  --text:#333333;
  --muted:#777777;
  --red-link:#d9362b;
  --rule:#d6d6d6;
  --footer:#2a4578;
  --footer-dark:#111111;
}
*{box-sizing:border-box;margin:0;padding:0}
html,body{width:1200px;height:3035px;overflow:hidden}
body{position:relative;font-family:"Roboto",Arial,sans-serif;color:var(--text);background:var(--white)}
a{color:inherit;text-decoration:none}

/* Hero */
.hero{position:absolute;left:0;top:0;width:1200px;height:613px;
  background:linear-gradient(180deg,#6e6a62 0%,#8b857a 30%,#5d574d 65%,#3a352e 100%);border-top:6px solid var(--purple)}
.hero-photo{position:absolute;inset:0;background:radial-gradient(ellipse at 45% 35%,rgba(190,180,160,.35),rgba(0,0,0,0) 60%)}
.brand{position:absolute;left:87px;top:0;width:213px;height:78px;background:var(--purple);border-radius:0 0 6px 6px;
  display:flex;align-items:center;justify-content:center;color:var(--white);font-family:"Open Sans",sans-serif;font-weight:700;font-size:32px}
.top-nav{position:absolute;right:100px;top:30px;display:flex;gap:34px;font-size:13px;font-weight:500;color:var(--white);letter-spacing:.3px}
.top-nav span{display:flex;align-items:center;gap:6px}
.top-nav svg{width:12px;height:12px;fill:var(--white)}
.slide-arrow{position:absolute;top:274px;width:34px;height:34px;border-radius:50%;background:rgba(0,0,0,.45);display:flex;align-items:center;justify-content:center}
.slide-arrow svg{width:14px;height:14px;stroke:var(--white);stroke-width:2.5;fill:none}
.hero-title{position:absolute;left:0;width:1200px;top:240px;text-align:center;color:var(--white);font-family:"Open Sans",sans-serif;font-weight:700;font-size:52px;letter-spacing:1px;text-shadow:0 2px 4px rgba(0,0,0,.4)}
.hero-sub{position:absolute;left:0;width:1200px;top:312px;text-align:center;color:var(--white);font-family:"Open Sans",sans-serif;font-weight:600;font-size:28px;text-shadow:0 2px 4px rgba(0,0,0,.4)}
.search-panel{position:absolute;left:208px;top:443px;width:780px;height:85px;background:rgba(255,255,255,.35);border-radius:4px}
.select{position:absolute;top:16px;height:57px;background:var(--white);border:1px solid #ccc;font-size:14px;color:#444;display:flex;align-items:center;padding-left:20px}
.select::after{content:"";position:absolute;right:18px;top:26px;border:5px solid transparent;border-top-color:#444}
.select.dest{left:23px;width:281px}
.select.act{left:320px;width:277px}
.go-btn{position:absolute;left:608px;top:16px;width:149px;height:57px;background:var(--purple-btn);border-radius:4px;color:var(--white);font-size:17px;font-weight:500;display:flex;align-items:center;justify-content:center}

/* Section heads */
.section{position:absolute;left:0;width:1200px}
.section.grey{background:var(--light-bg)}
.section-title{position:absolute;left:0;width:1200px;text-align:center;font-size:20px;font-weight:700;color:#222;letter-spacing:.3px}
.section-title em{font-style:normal;color:var(--purple)}
.title-rule{position:absolute;left:445px;width:310px;height:4px;background:var(--rule)}
.title-rule::after{content:"";position:absolute;left:135px;top:-1px;width:40px;height:4px;background:var(--accent)}

/* Tiles */
.tile{position:absolute;width:244px;height:188px;overflow:hidden}
.tile-label{position:absolute;left:0;bottom:0;width:100%;height:40px;background:rgba(0,0,0,.45);color:var(--white);font-size:17px;font-weight:700;display:flex;align-items:center;justify-content:center}
.more-link{position:absolute;left:0;width:1200px;text-align:center;font-size:15px;color:#333}

/* Blog */
.blog-head{position:absolute;left:93px;top:42px;font-size:20px;font-weight:500;color:#222}
.blog-arrows{position:absolute;left:1073px;top:40px;width:30px;height:22px}
.post{position:absolute;top:87px;width:326px}
.post-media{position:relative;width:326px;height:217px;border:3px solid var(--white)}
.play{position:absolute;left:50%;top:50%;width:70px;height:70px;margin:-35px 0 0 -35px}
.post-date{position:absolute;left:0;bottom:0;background:#222;color:var(--white);font-size:14px;padding:7px 12px}
.post-title{margin-top:16px;font-size:15px;font-weight:400;color:#333;display:flex;align-items:center;gap:14px}
.stars{color:var(--star);font-size:18px;letter-spacing:1px}
.post-text{margin-top:12px;font-size:11.5px;line-height:20px;color:var(--muted);padding-left:4px;width:310px}
.read-more{display:block;margin-top:12px;font-size:11.5px;color:var(--red-link);padding-left:4px}

/* SEO links */
.seo{background:linear-gradient(180deg,#34383a 0%,#272a2c 60%,#303230 100%)}
.seo .section-title{color:var(--white);font-weight:500;font-size:23px}
.seo-col{position:absolute;top:120px;list-style:none;color:var(--white);font-size:13px;line-height:29px}
.seo-col li::before{content:"";display:inline-block;border:4px solid transparent;border-left-color:var(--white);margin-right:8px;vertical-align:1px}

/* Footer */
.footer{background:var(--footer);color:var(--white)}
.foot-col{position:absolute;top:44px}
.foot-col h4{font-size:15px;font-weight:500;letter-spacing:.3px;margin-bottom:20px}
.foot-col ul{list-style:none;font-size:13px;line-height:25px}
.news-text{font-size:11.5px;line-height:18px;width:220px;margin-top:-6px}
.news-form{display:flex;margin-top:14px}
.news-input{width:142px;height:32px;background:var(--white);color:#999;font-size:11px;padding:9px 10px}
.news-btn{width:64px;height:32px;background:#161616;font-size:12px;display:flex;align-items:center;justify-content:center}
.social{display:flex;gap:14px;margin-top:18px;list-style:none;font-size:12px}
.social li{display:flex;align-items:center;gap:6px}
.social li::before{content:"";width:12px;height:12px;border:2px solid var(--white);border-radius:50%}
.copyright{background:var(--footer-dark);color:var(--white);font-size:12px;display:flex;align-items:center;justify-content:center}
</style>
</head>
<body>

<header class="hero">
  <div class="hero-photo" role="img" aria-label="Couple taking a selfie on a rocky summit above a misty coastline"></div>
  <div class="brand">uTrundle</div>
  <nav class="top-nav">
    <span><svg viewBox="0 0 12 12"><path d="M6 11 1 6a3 3 0 0 1 5-4 3 3 0 0 1 5 4z"/></svg>WISHLIST</span>
    <span><svg viewBox="0 0 12 12"><path d="M0 1h2l2 7h7l1-5H3"/><circle cx="5" cy="10.5" r="1"/><circle cx="10" cy="10.5" r="1"/></svg>CART</span>
    <span><svg viewBox="0 0 12 12"><circle cx="6" cy="6" r="6"/></svg>LANGUAGE</span>
    <span>( $ ) CURRENCY</span>
    <span><svg viewBox="0 0 12 12"><circle cx="6" cy="6" r="6"/></svg>HELP</span>
    <span><svg viewBox="0 0 12 12"><circle cx="6" cy="3.5" r="3"/><path d="M0 12a6 5 0 0 1 12 0z"/></svg>LOG IN</span>
  </nav>
  <div class="slide-arrow" style="left:56px"><svg viewBox="0 0 14 14"><path d="M9 2 4 7l5 5"/></svg></div>
  <div class="slide-arrow" style="left:1112px"><svg viewBox="0 0 14 14"><path d="m5 2 5 5-5 5"/></svg></div>
  <h1 class="hero-title">BOOK ACTIVITIES</h1>
  <p class="hero-sub">YOUR ADVENTURE STARTS HERE!</p>
  <div class="search-panel">
    <div class="select dest">Choose a destination</div>
    <div class="select act">Choose an activity</div>
    <div class="go-btn">LET'S GO!</div>
  </div>
</header>

<section class="section grey" style="top:613px;height:636px">
  <h2 class="section-title" style="top:43px">MOST POPULAR <em>DESTINATIONS</em></h2>
  <div class="title-rule" style="top:83px"></div>
  <div class="tile" style="left:89px;top:126px;background:linear-gradient(160deg,#8fb2cc,#c43b3b 60%,#7a2424)" role="img" aria-label="Group cheering on a boat trip in Tenerife"><div class="tile-label">Tenerife</div></div>
  <div class="tile" style="left:348px;top:126px;background:linear-gradient(180deg,#5a8cc4,#a9c0d8 40%,#b8882e 75%,#5f4a1e)" role="img" aria-label="Helicopter flying over autumn hills in Lanzarote"><div class="tile-label">Lanzarote</div></div>
  <div class="tile" style="left:607px;top:126px;background:linear-gradient(170deg,#7a5a44,#9b7457 50%,#5c3f2d)" role="img" aria-label="Quad bikes on a dusty track in Fuerteventura"><div class="tile-label">Fuerteventura</div></div>
  <div class="tile" style="left:868px;top:126px;background:linear-gradient(180deg,#9cb5d0,#b59a6d 45%,#6d5534)" role="img" aria-label="Hiker walking through dry hills in Gran Canaria"><div class="tile-label">Gran Canaria</div></div>
  <div class="tile" style="left:89px;top:334px;background:linear-gradient(170deg,#4f7d3a,#8ba867 50%,#3a5a27)" role="img" aria-label="Lush garden with palm trees in El Hierro"><div class="tile-label">El Hierro</div></div>
  <div class="tile" style="left:348px;top:334px;background:linear-gradient(180deg,#6f9fd6,#d9dfe5 45%,#7e7f6e 75%,#3d5a2e)" role="img" aria-label="Historic white building with palm trees in La Palma"><div class="tile-label">La Palma</div></div>
  <div class="tile" style="left:607px;top:334px;background:linear-gradient(150deg,#9b4a36,#6a3526 50%,#3d3d3d)" role="img" aria-label="Red volcanic rock formations in Porto Santo"><div class="tile-label">Porto Santo</div></div>
  <div class="tile" style="left:868px;top:334px;background:linear-gradient(180deg,#6aa2cf,#8d5a44 45%,#7b6b4e 80%,#4a5a34)" role="img" aria-label="Volcanic crater landscape in Madeira"><div class="tile-label">Madeira</div></div>
  <a class="more-link" style="top:556px">More popular destinations »</a>
</section>

<section class="section" style="top:1249px;height:647px">
  <h2 class="section-title" style="top:54px">MOST POPULAR ACTIVITIES</h2>
  <div class="title-rule" style="top:94px"></div>
  <div class="tile" style="left:89px;top:133px;background:linear-gradient(180deg,#5f93cf,#a8c4e0 45%,#7d6a52 70%,#4c3f30)" role="img" aria-label="Road cyclist riding below a volcano in Tenerife"><div class="tile-label">Tenerife</div></div>
  <div class="tile" style="left:348px;top:133px;background:linear-gradient(180deg,#5f93cf,#a7bfd6 40%,#c9955a 70%,#a2672f)" role="img" aria-label="Mountain biker on a coastal trail in Lanzarote"><div class="tile-label">Lanzarote</div></div>
  <div class="tile" style="left:607px;top:133px;background:linear-gradient(170deg,#1f6fb8,#2f8fd6 50%,#14487e)" role="img" aria-label="Dolphin leaping in blue sea off Fuerteventura"><div class="tile-label">Fuerteventura</div></div>
  <div class="tile" style="left:868px;top:133px;background:linear-gradient(180deg,#4f8ad0,#9fb8d4 45%,#8a8272 70%,#5a5448)" role="img" aria-label="Hikers on a rocky ridge in Gran Canaria"><div class="tile-label">Gran Canaria</div></div>
  <div class="tile" style="left:89px;top:342px;background:linear-gradient(180deg,#2aa7d6,#43c6d8 50%,#1d7fa6)" role="img" aria-label="Turquoise bay with a sailing boat in El Hierro"><div class="tile-label">El Hierro</div></div>
  <div class="tile" style="left:348px;top:342px;background:linear-gradient(150deg,#6fa0d4,#b39a72 40%,#8a6c44 70%,#3c6e8c)" role="img" aria-label="Walkers on a cliff path above the sea in La Palma"><div class="tile-label">La Palma</div></div>
  <div class="tile" style="left:607px;top:342px;background:linear-gradient(180deg,#2d5a7a,#3b6d8e 50%,#e3c21c 72%,#2a5170)" role="img" aria-label="Riders on an inflatable banana boat in Porto Santo"><div class="tile-label">Porto Santo</div></div>
  <div class="tile" style="left:868px;top:342px;background:linear-gradient(170deg,#dfe4e8,#c9d2da 40%,#c23232 65%,#6d8ea8)" role="img" aria-label="Rider on a jet ski in Madeira"><div class="tile-label">Madeira</div></div>
  <a class="more-link" style="top:566px">More popular destinations »</a>
</section>

<section class="section grey" style="top:1896px;height:522px">
  <h2 class="blog-head">LATEST BLOG</h2>
  <svg class="blog-arrows" viewBox="0 0 30 22"><path d="M11 4 4 11l7 7M19 4l7 7-7 7" stroke="#222" stroke-width="2.5" fill="none"/></svg>

  <article class="post" style="left:91px">
    <div class="post-media" style="background:linear-gradient(150deg,#3a2a20,#8a7460 45%,#2a1e16)" role="img" aria-label="Close-up of a succulent plant on dark rock">
      <svg class="play" viewBox="0 0 70 70"><circle cx="35" cy="35" r="32" fill="rgba(0,0,0,.45)" stroke="#fff" stroke-width="3"/><path d="M28 22v26l20-13z" fill="#fff"/></svg>
      <span class="post-date">21/ 05/2016</span>
    </div>
    <h3 class="post-title">Neque porro quisquam <span class="stars">★★★★★</span></h3>
    <p class="post-text">Lorem Ipsum has been the industry's standard dummy text ever since the 1500s, when an unknown printer</p>
    <a class="read-more">Read More &gt;&gt;</a>
  </article>

  <article class="post" style="left:439px">
    <div class="post-media" style="background:linear-gradient(180deg,#c9d7e3,#d8e1e8 55%,#6b8aa0 75%,#a9b6bf)" role="img" aria-label="Kitesurfer jumping over waves near a beach">
      <svg class="play" viewBox="0 0 70 70"><circle cx="35" cy="35" r="32" fill="rgba(0,0,0,.45)" stroke="#fff" stroke-width="3"/><path d="M28 22v26l20-13z" fill="#fff"/></svg>
      <span class="post-date">21/ 05/2016</span>
    </div>
    <h3 class="post-title">Neque porro quisquam est <span class="stars">★★★★★</span></h3>
    <p class="post-text">Lorem Ipsum has been the industry's standard dummy text ever since the 1500s, when an unknown printer</p>
    <a class="read-more">Read More &gt;&gt;</a>
  </article>

  <article class="post" style="left:785px">
    <div class="post-media" style="background:linear-gradient(160deg,#8a9a7a,#c8c1b0 45%,#6d8aa8 75%,#d8d4cc)" role="img" aria-label="Group of travellers sitting together indoors">
      <svg class="play" viewBox="0 0 70 70"><circle cx="35" cy="35" r="32" fill="rgba(0,0,0,.45)" stroke="#fff" stroke-width="3"/><path d="M28 22v26l20-13z" fill="#fff"/></svg>
      <span class="post-date">21/ 05/2016</span>
    </div>
    <h3 class="post-title">Neque porro quisquam est <span class="stars">★★★★★</span></h3>
    <p class="post-text">Lorem Ipsum has been the industry's standard dummy text ever since the 1500s, when an unknown printer</p>
    <a class="read-more">Read More &gt;&gt;</a>
  </article>

  <a class="more-link" style="top:466px">Show more »</a>
</section>

<section class="section seo" style="top:2418px;height:324px" role="img" aria-label="Dark rocky coastline at dusk behind travel link list">
  <h2 class="section-title" style="top:40px">USEFUL FOR SEO</h2>
  <ul class="seo-col" style="left:91px">
    <li>Top things to do in Tenerife!</li><li>Top things to do in Barcelona</li><li>Top things to do in Paris!</li>
    <li>Top things to do in London!</li><li>Top things to do in Berlin!</li><li>Top things to do in Kuala Lumpur!</li>
  </ul>
  <ul class="seo-col" style="left:364px">
    <li>Top things to do in Barcelona!</li><li>Top things to do in Barcelona!</li><li>Top things to do in Barcelona!</li>
    <li>Top things to do in Barcelona!</li><li>Top things to do in Barcelona!</li><li>Top things to do in Barcelona!</li>
  </ul>
  <ul class="seo-col" style="left:643px">
    <li>Top things to do in Tenerife!</li><li>Top things to do in Barcelona</li><li>Top things to do in Paris!</li>
    <li>Top things to do in London!</li><li>Top things to do in Berlin!</li><li>Top things to do in Paris!</li>
  </ul>
  <ul class="seo-col" style="left:911px">
    <li>Top things to do in Barcelona!</li><li>Top things to do in Barcelona!</li><li>Top things to do in Barcelona!</li>
    <li>Top things to do in Barcelona!</li><li>Top things to do in Barcelona!</li><li>Top things to do in Barcelona!</li>
  </ul>
</section>

<footer class="section footer" style="top:2742px;height:225px">
  <div class="foot-col" style="left:91px"><h4>COMPANY</h4>
    <ul><li>About uTrundle.net</li><li>Corporate Info</li><li>Site map?</li><li>Blog</li><li>Careers</li></ul></div>
  <div class="foot-col" style="left:328px"><h4>SUPPORT</h4>
    <ul><li>Contact us</li><li>FAQs</li><li>Legal</li><li>Privacy Policy</li><li>Legal</li></ul></div>
  <div class="foot-col" style="left:510px"><h4>PARTNERSHIPS</h4>
    <ul><li>Supplier sign-up</li><li>Affiliate Programs</li></ul></div>
  <div class="foot-col" style="left:739px"><h4>LOG-INS</h4>
    <ul><li>Customers</li><li>Suppliers</li><li>Affiliates</li></ul></div>
  <div class="foot-col" style="left:898px"><h4>NEWSLETTER</h4>
    <p class="news-text">Your about us information would fit here nicely.</p>
    <div class="news-form"><span class="news-input">Email address</span><span class="news-btn">Submit</span></div>
    <ul class="social"><li>Kivo</li><li>Tweel</li><li>Shutra</li></ul>
  </div>
</footer>

<div class="section copyright" style="top:2967px;height:68px">Copyright © 2015. All Rights Reserved</div>

</body>
</html>
```